Software company specialized in data analytics and professional services

We need a landing page design for our business. It should include our logo design. It should have multiple sections :
- stylish head
- what we do (data analytics software, professional services)
- contact form

Target Market(s)

Companies, B2B

Industry/Entity Type

Data

Number of Pages Required

1 page

Font styles to use
Sans Serif

Requirements
Must have
• Dark theme
Should not have
• Gradients on buttons

```html
<!DOCTYPE html>
<html lang="en">
<head>
<meta charset="utf-8">
<title>NovaGrid – Data Analytics &amp; Professional Services</title>
<link href="https://fonts.googleapis.com/css2?family=Poppins:wght@400;500;600;700&display=swap" rel="stylesheet">
<style>
:root{
  --magenta:#c21bc0;
  --magenta-soft:#e04ad9;
  --pink:#ee2f9e;
  --violet:#7d1ee6;
  --navy:#121a45;
  --navy-deep:#0d1230;
  --teal:#0d6a8f;
  --bg:#0e1327;
  --bg-alt:#151b35;
  --card:#19203f;
  --text:#eef0f6;
  --muted:#b3b7c8;
  --field-text:#8f92a1;
  --white:#ffffff;
  --line:#9b2fe0;
}
*{box-sizing:border-box;margin:0;padding:0}
html,body{width:1200px;height:3797px;overflow:hidden}
body{font-family:'Poppins',sans-serif;color:var(--text);background:var(--bg);position:relative}
.abs{position:absolute}

/* header */
.site-header{position:absolute;top:0;left:0;width:1200px;height:61px;background:var(--bg)}
.brand{left:140px;top:14px;font-size:29px;font-weight:600;color:var(--magenta-soft);letter-spacing:1px}
.contact-chip{top:14px;display:flex;gap:10px;align-items:center;font-size:12px;line-height:16px;color:var(--text)}
.contact-chip svg{width:28px;height:28px}

/* hero */
.hero{top:61px;left:0;width:1200px;height:551px;background:linear-gradient(90deg,#1a2436 0%,#223047 45%,#3a4450 70%,#2c3038 100%)}
.hero-photo{right:0;top:0;width:560px;height:551px;background:radial-gradient(circle at 55% 45%,#5d6877 0%,#39424f 45%,#23293a 100%)}
.hero h1{left:142px;top:148px;font-size:35px;line-height:45px;font-weight:700;color:var(--white);text-transform:uppercase}
.hero h1 span{color:var(--magenta)}
.hero p{left:142px;top:290px;width:400px;font-size:14px;line-height:23px;color:#e7e9ef}
.btn-hero{left:141px;top:360px;width:166px;height:35px;border-radius:18px;background:var(--magenta);color:var(--white);font-size:12px;display:flex;align-items:center;justify-content:center}

/* section titles */
.sec-title{left:0;width:1200px;text-align:center;font-size:37px;font-weight:600;color:var(--magenta-soft)}
.sec-title::before{content:"";position:absolute;left:50%;top:-8px;width:34px;height:4px;margin-left:-17px;background:var(--magenta-soft);border-radius:2px}

/* services */
.tab{top:786px;height:50px;width:248px;border-radius:0 22px 0 22px;font-size:15px;font-weight:600;display:flex;align-items:center;justify-content:center}
.tab-outline{left:338px;border:2px solid var(--line);color:var(--text)}
.tab-active{left:615px;background:var(--teal);color:var(--white)}
.service-card{width:214px;height:199px;border:2px solid var(--line);border-radius:0 22px 0 22px;padding:24px 20px 0 20px;background:var(--card)}
.service-card svg{width:44px;height:44px;display:block}
.service-card h3{margin-top:14px;font-size:14px;font-weight:600;color:var(--text)}
.service-card p{margin-top:10px;font-size:12.5px;line-height:20px;color:var(--muted)}

/* about */
.about{top:1389px;left:0;width:1200px;height:616px;background:var(--bg-alt)}
.about-photo{left:183px;top:86px;width:374px;height:403px;border-radius:0 60px 0 60px;background:linear-gradient(135deg,#c7ccd6 0%,#7b8494 45%,#3c4b6b 100%)}
.badge-dark{left:128px;top:135px;width:190px;height:84px;border-radius:0 20px 0 20px;background:linear-gradient(90deg,var(--navy-deep),var(--teal));color:var(--white);padding:26px 0 0 34px;font-size:13px;line-height:19px}
.badge-dark b{font-weight:600}
.stat-card{background:var(--card);border-radius:0 20px 0 20px;box-shadow:0 8px 22px rgba(0,0,0,.35);text-align:center;padding-top:14px}
.stat-card strong{display:block;font-size:35px;font-weight:600;line-height:44px;color:var(--text)}
.stat-card span{font-size:13px;color:var(--text)}
.ring{width:22px;height:22px;border:2px solid var(--magenta-soft);border-radius:50%}
.ring::after{content:"";position:absolute;left:5px;top:5px;width:8px;height:8px;border-radius:50%;background:var(--magenta-soft)}
.about h2{left:639px;top:102px;font-size:37px;font-weight:600;color:var(--magenta-soft)}
.about h2::before{content:"";position:absolute;left:2px;top:-8px;width:34px;height:4px;background:var(--magenta-soft);border-radius:2px}
.about .lead{left:639px;top:162px;width:430px;font-size:13px;line-height:20.5px;color:var(--muted)}
.bullet{left:639px;width:430px;padding-left:35px;font-size:13px;line-height:20.5px;color:var(--muted)}
.bullet::before{content:"";position:absolute;left:0;top:9px;width:20px;height:3px;background:var(--magenta-soft)}
.btn-dark{left:639px;top:434px;width:154px;height:43px;border-radius:0 18px 0 0;background:var(--teal);color:var(--white);font-size:13px;font-weight:600;display:flex;align-items:center;justify-content:center}

/* newsletter */
.newsletter{left:140px;top:2091px;width:918px;height:331px;border-radius:0 80px 0 80px;background:linear-gradient(90deg,var(--violet) 0%,#b024c8 50%,var(--pink) 100%);color:var(--white);text-align:center}
.newsletter .kicker{position:absolute;left:0;width:100%;top:80px;font-size:12.5px}
.newsletter h2{position:absolute;left:0;width:100%;top:100px;font-size:37px;font-weight:600}
.email-field{left:230px;top:169px;width:312px;height:40px;background:var(--white);border-radius:0 0 0 20px;color:var(--field-text);font-size:13px;text-align:left;padding:11px 0 0 27px}
.btn-sub{left:542px;top:169px;width:147px;height:40px;background:var(--navy-deep);border-radius:0 20px 0 0;font-size:13px;font-weight:600;display:flex;align-items:center;justify-content:center}
.newsletter .note{position:absolute;left:0;width:100%;top:238px;font-size:12.5px}

/* testimonial */
.testimonials{top:2508px;left:0;width:1200px;height:647px;background:var(--bg-alt)}
.testimonials .intro{left:290px;top:150px;width:620px;text-align:center;font-size:13px;line-height:20.5px;color:var(--text)}
.avatar{border-radius:50%;background:linear-gradient(160deg,#c9ced8,#6e7a90)}
.quote-box{left:318px;top:360px;width:564px;height:132px;border-radius:0 40px 0 0;background:linear-gradient(90deg,var(--navy-deep),var(--teal));color:var(--white);text-align:center;font-size:13px;line-height:20.5px;padding:24px 30px 0}
.person{left:0;width:1200px;top:526px;text-align:center}
.person b{display:block;font-size:14px;font-weight:600}
.person span{font-size:12px;color:var(--muted)}
.arrow{width:30px;height:30px;border-radius:50%;display:flex;align-items:center;justify-content:center}

/* contact */
.contact{top:3155px;left:0;width:1200px;height:605px;background:linear-gradient(90deg,var(--violet) 0%,#b024c8 50%,var(--pink) 100%);color:var(--white)}
.contact h2{left:0;width:1200px;top:94px;text-align:center;font-size:37px;font-weight:600}
.contact h2::before{content:"";position:absolute;left:50%;top:-8px;width:34px;height:4px;margin-left:-17px;background:var(--white);border-radius:2px}
.contact .sub{left:0;width:1200px;top:153px;text-align:center;font-size:13px}
.form-panel{left:183px;top:207px;width:417px;height:313px;border-radius:0 60px 0 60px;background:linear-gradient(90deg,var(--navy-deep),var(--teal))}
.field{background:var(--white);border-radius:4px;height:34px;color:var(--field-text);font-size:12.5px;padding:8px 0 0 20px}
.btn-submit{left:28px;top:230px;width:362px;height:42px;border-radius:0 18px 0 18px;background:var(--magenta);font-size:13px;font-weight:600;display:flex;align-items:center;justify-content:center}
.info{left:642px;width:240px;font-size:13px;line-height:20.5px}
.info b{display:block;font-weight:600;margin-bottom:9px;position:relative}
.info b::before{content:"";position:absolute;left:0;top:-5px;width:18px;height:2px;background:var(--navy)}
.site-footer{top:3760px;left:0;width:1200px;height:37px;background:var(--navy-deep);color:var(--white);text-align:center;font-size:12.5px;line-height:37px}
</style>
</head>
<body>

<header class="site-header">
  <div class="abs brand">NOVAGRID</div>
  <div class="abs contact-chip" style="left:765px">
    <svg viewBox="0 0 28 28" fill="none" stroke="#e04ad9" stroke-width="1.6"><path d="M6 5l4 0 2 5-3 2c1 3 3 5 6 6l2-3 5 2v4c0 1-1 2-2 2C11 23 5 17 4 7c0-1 1-2 2-2z"/></svg>
    <div>CALL US<br>+ 555 010 2040</div>
  </div>
  <div class="abs contact-chip" style="left:910px">
    <svg viewBox="0 0 28 28" fill="none" stroke="#e04ad9" stroke-width="1.6"><rect x="3" y="8" width="22" height="15" rx="1"/><path d="M3 8l11 9 11-9"/></svg>
    <div>EMAIL US<br>info@novagrid.com</div>
  </div>
</header>

<section class="abs hero">
  <div class="abs hero-photo" role="img" aria-label="Photo of a businessman using a laptop with a glowing globe and data overlay"></div>
  <h1 class="abs">Helping <span>Businesses</span><br>Succeed With<br>IT Technology</h1>
  <p class="abs">Lorem ipsum dolor sit amet, consectetuer adipiscing<br>elit, sed diam nonummy nibh euismod tincidunt.</p>
  <div class="abs btn-hero">CONTACT US TODAY</div>
</section>

<h2 class="abs sec-title" style="top:704px">Our Services</h2>
<div class="abs tab tab-outline">DATA ANALYTICS</div>
<div class="abs tab tab-active">PROFESSIONAL SERVICES</div>

<div class="abs service-card" style="left:140px;top:878px">
  <svg viewBox="0 0 44 44" fill="none" stroke="#e04ad9" stroke-width="2.4"><circle cx="18" cy="18" r="13"/><path d="M28 28l11 11"/><path d="M12 23v-5M18 23v-9M24 23v-7"/></svg>
  <h3>Data Analytics</h3><p>Lorem ipsum dolor sit aet, consectetur adiscing elit, sed do.</p>
</div>
<div class="abs service-card" style="left:375px;top:878px">
  <svg viewBox="0 0 44 44" fill="none" stroke="#e04ad9" stroke-width="2.4"><path d="M6 18h8l16-10v28L14 26H6z"/><path d="M10 26l3 10h5l-2-10"/><path d="M34 16c3 2 3 8 0 10"/></svg>
  <h3>Marketing Analysis</h3><p>Lorem ipsum dolor sit aet, consectetur adiscing elit, sed do.</p>
</div>
<div class="abs service-card" style="left:609px;top:878px">
  <svg viewBox="0 0 44 44" fill="none" stroke="#e04ad9" stroke-width="2.2"><rect x="4" y="4" width="36" height="10" rx="2"/><rect x="4" y="17" width="36" height="10" rx="2"/><rect x="4" y="30" width="36" height="10" rx="2"/><path d="M9 9h3M9 22h3M9 35h3M20 9h14M20 22h14M20 35h14"/></svg>
  <h3>Server Analysis</h3><p>Lorem ipsum dolor sit aet, consectetur adiscing elit, sed do.</p>
</div>
<div class="abs service-card" style="left:843px;top:878px">
  <svg viewBox="0 0 44 44" fill="#e04ad9"><circle cx="22" cy="6" r="3"/><rect x="21" y="7" width="2" height="6"/><path d="M8 24a14 12 0 0 1 28 0v6a10 8 0 0 1-10 8h-8A10 8 0 0 1 8 30z"/><circle cx="16" cy="25" r="3" fill="#19203f"/><circle cx="28" cy="25" r="3" fill="#19203f"/></svg>
  <h3>Machine Learning</h3><p>Lorem ipsum dolor sit aet, consectetur adiscing elit, sed do.</p>
</div>
<div class="abs service-card" style="left:375px;top:1098px">
  <svg viewBox="0 0 44 44" fill="none" stroke="#e04ad9" stroke-width="2.4"><path d="M4 22c5-8 11-12 18-12s13 4 18 12c-5 8-11 12-18 12S9 30 4 22z"/><circle cx="22" cy="22" r="6" fill="#e04ad9"/><path d="M22 2v5M8 6l3 4M36 6l-3 4M22 37v5"/></svg>
  <h3>Data Visualization</h3><p>Lorem ipsum dolor sit aet, consectetur adiscing elit, sed do.</p>
</div>
<div class="abs service-card" style="left:609px;top:1098px">
  <svg viewBox="0 0 44 44" fill="none" stroke="#e04ad9" stroke-width="2"><path d="M4 24l8-8 8 6 12-6 8 8-12 12-6-4-6 2z"/><path d="M14 16l8 2M20 28l4 4M16 30l3 3"/><path d="M22 8l6-4 6 6M34 4v6h-6"/></svg>
  <h3>Business Intelligence</h3><p>Lorem ipsum dolor sit aet, consectetur adiscing elit, sed do.</p>
</div>

<section class="abs about">
  <div class="abs about-photo" role="img" aria-label="Photo of a person reviewing analytics dashboards on a laptop"></div>
  <div class="abs badge-dark"><b>DATA ANALYTICS</b><br>Lorem ipsum dolor</div>
  <div class="abs stat-card" style="left:465px;top:149px;width:160px;height:99px"><strong>99+</strong><span>Satisfied Customers</span></div>
  <div class="abs stat-card" style="left:372px;top:437px;width:163px;height:99px"><strong>300+</strong><span>Project Completed</span></div>
  <div class="abs ring" style="left:1039px;top:83px"></div>
  <div class="abs ring" style="left:142px;top:489px"></div>
  <h2 class="abs">About Us</h2>
  <p class="abs lead">Lorem ipsum dolor sit amet, consectetur adipiscing elit, sed do eiusmod tempor incididunt ut labore et dolore magna aliqua. Ut enim ad minim veniam, quis nostrud exercitation ullamco laboris nisi ut aliquip ex ea commodo consequat. Duis aute irure dolor in reprehenderit in voluptate velit esse cillum dolore eu fugiat nulla pariatur. Excepteur sint occaecat cupidatat non proident, sunt in culpa qui officia deserunt mollit anim id est laborum.</p>
  <p class="abs bullet" style="top:321px">Lorem ipsum dolor sit amet, consectetur adipiscing elit, sed do eiusmod tempor</p>
  <p class="abs bullet" style="top:377px">Lorem ipsum dolor sit amet, consectetur adipiscing elit,</p>
  <div class="abs btn-dark">GET STARTED</div>
</section>

<section class="abs newsletter">
  <div class="kicker">Get Latest News From Us</div>
  <h2>Subscribe to Our Newsletter</h2>
  <div class="abs email-field">Your Email</div>
  <div class="abs btn-sub">SUBSCRIBE</div>
  <div class="note">We Won't Send Any Spams. Promise!</div>
</section>

<section class="abs testimonials">
  <h2 class="abs sec-title" style="top:84px">Client Testimonial</h2>
  <p class="abs intro">Lorem ipsum dolor sit amet, consectetur adipiscing elit, sed do eiusmod tempor incididunt ut labore et dolore magna aliqua. Ut enim ad minim veniam.</p>
  <div class="abs avatar" style="left:547px;top:225px;width:105px;height:105px" role="img" aria-label="Portrait of the featured client"></div>
  <div class="abs avatar" style="left:220px;top:295px;width:50px;height:50px" role="img" aria-label="Client portrait"></div>
  <div class="abs avatar" style="left:943px;top:295px;width:40px;height:40px" role="img" aria-label="Client portrait"></div>
  <div class="abs avatar" style="left:985px;top:407px;width:50px;height:50px" role="img" aria-label="Client portrait"></div>
  <div class="abs avatar" style="left:193px;top:461px;width:36px;height:36px" role="img" aria-label="Client portrait"></div>
  <div class="abs avatar" style="left:942px;top:526px;width:35px;height:35px" role="img" aria-label="Client portrait"></div>
  <div class="abs quote-box">Lorem ipsum dolor sit amet, consectetur adipiscing elit, sed do eiusmod tempor incididunt ut labore et dolore magna aliqua. Ut enim ad minim veniam, quis nostrud exercitation ullamco laboris nisi ut aliquip ex ea commodo.</div>
  <div class="abs person"><b>Alan Verity</b><span>Lorem ipsum</span></div>
  <div class="abs arrow" style="left:488px;top:539px;border:2px solid var(--magenta-soft)">
    <svg width="14" height="14" viewBox="0 0 14 14" fill="none" stroke="#e04ad9" stroke-width="2"><path d="M13 7H2M6 3L2 7l4 4"/></svg>
  </div>
  <div class="abs arrow" style="left:691px;top:539px;background:var(--teal)">
    <svg width="14" height="14" viewBox="0 0 14 14" fill="none" stroke="#fff" stroke-width="2"><path d="M1 7h11M8 3l4 4-4 4"/></svg>
  </div>
</section>

<section class="abs contact">
  <h2 class="abs">Get in Touch With Us</h2>
  <p class="abs sub">You are clicksaway from your technological future</p>
  <div class="abs form-panel">
    <div class="abs field" style="left:28px;top:45px;width:174px">Name*</div>
    <div class="abs field" style="left:216px;top:45px;width:174px">Email*</div>
    <div class="abs field" style="left:28px;top:95px;width:174px">Phone Number*</div>
    <div class="abs field" style="left:216px;top:95px;width:174px">Company Name</div>
    <div class="abs field" style="left:28px;top:145px;width:362px;height:69px">Your Message</div>
    <div class="abs btn-submit">SUBMIT</div>
  </div>
  <div class="abs info" style="top:264px"><b>Address</b>123, Lorem ipsum dolor sit aet,<br>consectetur adiscing.</div>
  <div class="abs info" style="top:358px"><b>Phone Number</b>555 010 2040</div>
  <div class="abs info" style="top:434px"><b>Email Address</b>info@novagrid.com</div>
</section>

<footer class="abs site-footer">© 2023 NovaGrid Data Analytics. All Rights Reserved.</footer>

</body>
</html>
```